Real estate company needs a letterhead design

A young real estate company needs a letterhead / stationery design, it should include the company's logo. It should look exactly the same as on the business cards. (With the phrase "a brand of KEV Wohnbau & Grundstücksentwicklung GmbH")

In addition, it should also include the 4 round seals.

color code blue # 00456b gray # 333333

Word and PDF are welcome.

KEV Wohnbau & Grundstücksentwicklung GmbH
Managing director: Mag. Lukas Fellnhuber
Matthias-Ortner-Strasse 3c / 41
6391 Talbrunn

Tel .: +436648172093
Email: office@wohnglanz-beispiel.at
Web: www.wohnglanz-beispiel.at

Sparkasse Almtal, Bergländer Sparkasse from 1882, Genossenschaftskasse
Anton-Weissauer-Strasse 7, 6391 Talbrunn
IBAN: AT31 4817 2964 0058 2316
BIC: GLMTAT44XXX
Account holder: KEV Wohnbau & Grundstücksentwicklung GmbH

FN: XXXXXXX
UID: XXXXXXX

```html
<!DOCTYPE html>
<html lang="de">
<head>
<meta charset="utf-8">
<title>Wohnglanz Briefpapier</title>
<link rel="stylesheet" href="https://fonts.googleapis.com/css2?family=Asap+Condensed:wght@400&family=Lato:wght@400&family=Montserrat:wght@300;400;600;700&display=swap">
<style>
  :root {
    --brand-blue: #00456b;
    --band-blue: #06476c;
    --text-gray: #5b5b5b;
    --ink-gray: #333333;
    --page-bg: #d6d6d6;
    --paper: #ffffff;
    --rule: rgba(255,255,255,0.85);
  }
  * { margin: 0; padding: 0; box-sizing: border-box; }
  html, body { width: 1056px; height: 1200px; overflow: hidden; background: var(--page-bg); }
  .letterhead {
    position: absolute; left: 118px; top: 20px;
    width: 820px; height: 1160px;
    background: var(--paper);
    box-shadow: 0 6px 24px rgba(0,0,0,0.18);
  }
  .sidebar {
    position: absolute; left: 0; top: 0; width: 256px; height: 100%;
    background: var(--band-blue); color: #fff;
    font-family: 'Montserrat', sans-serif;
  }
  .sidebar > * { position: absolute; left: 26px; }
  .double-rule {
    width: 199px; height: 5px;
    border-top: 1px solid var(--rule); border-bottom: 1px solid var(--rule);
  }
  .contact-person { top: 690px; }
  .contact-person .name { font-size: 18.5px; font-weight: 700; line-height: 22px; white-space: nowrap; }
  .contact-person .role { font-size: 13.5px; font-weight: 400; line-height: 18px; letter-spacing: 0.2px; }
  .address { top: 772px; font-size: 13.5px; line-height: 16px; letter-spacing: 0.1px; white-space: nowrap; }
  .contact-list { top: 847px; list-style: none; font-size: 13.5px; line-height: 18px; }
  .contact-list li { display: flex; align-items: center; gap: 13px; white-space: nowrap; }
  .contact-list svg { width: 13px; height: 13px; flex: none; }
  .bank-details { top: 948px; font-size: 12.2px; line-height: 21px; white-space: nowrap; }
  .bank-details b { font-weight: 700; }

  .content { position: absolute; left: 290px; top: 0; width: 492px; color: var(--text-gray); }
  .content > * { position: absolute; left: 0; }
  .brand { top: 80px; }
  .brand-name {
    font-family: 'Montserrat', sans-serif; font-weight: 700;
    font-size: 44px; line-height: 50px; color: var(--brand-blue); letter-spacing: -0.5px;
    white-space: nowrap;
  }
  .brand-tagline {
    font-family: 'Lato', sans-serif; font-size: 9.6px; color: var(--ink-gray);
    white-space: nowrap; margin-top: -2px;
  }
  .date { top: 310px; font-family: 'Montserrat', sans-serif; font-weight: 300; font-size: 18px; }
  .recipient { top: 340px; font-family: 'Montserrat', sans-serif; font-weight: 700; font-size: 28px; line-height: 34px; color: #575757; letter-spacing: 0.2px; }
  .recipient-title { top: 382px; font-family: 'Montserrat', sans-serif; font-weight: 300; font-size: 18px; }
  .body-text { top: 455px; width: 492px; font-family: 'Asap Condensed', sans-serif; font-size: 17px; line-height: 28.5px; }
  .body-text .line { display: block; white-space: nowrap; text-align: justify; text-align-last: justify; }
  .body-text .line.last { text-align-last: left; }
  .body-text p + p { margin-top: 28.5px; }
  .closing { top: 862px; font-family: 'Asap Condensed', sans-serif; font-size: 18px; line-height: 28px; }
  .signature { top: 912px; width: 112px; height: 52px; background: linear-gradient(90deg, #dfe7ee, #eef2f6); border-radius: 4px; }

  .footer { position: absolute; left: 256px; right: 0; top: 1080px; text-align: center; }
  .footer .company { font-family: 'Montserrat', sans-serif; font-weight: 700; font-size: 13px; line-height: 18px; color: var(--brand-blue); }
  .footer .bank { font-family: 'Lato', sans-serif; font-size: 13px; line-height: 16px; color: #6a6a6a; }
</style>
</head>
<body>
<div class="letterhead">
  <aside class="sidebar">
    <div class="double-rule" style="top:661px"></div>
    <div class="contact-person">
      <div class="name">Mag. Lukas Fellnhuber</div>
      <div class="role">Managing director</div>
    </div>
    <div class="double-rule" style="top:753px"></div>
    <div class="address">Matthias-Ortner-Strasse<br>3c / 41 6391 Talbrunn</div>
    <div class="double-rule" style="top:823px"></div>
    <ul class="contact-list">
      <li><svg viewBox="0 0 16 16" fill="#fff"><path d="M3.6 1.5l2.3 2.8-1.3 1.6c.9 2 2.5 3.6 4.5 4.5l1.6-1.3 2.8 2.3-1.4 2.1C7.3 13.3 2.7 8.7 1.5 3z"/></svg>+436648172093</li>
      <li><svg viewBox="0 0 16 16" fill="#fff"><path d="M1 3.5h14v9H1z M1.6 4l6.4 5 6.4-5" stroke="#06476c" stroke-width="1"/></svg>office@wohnglanz-beispiel.at</li>
      <li><svg viewBox="0 0 16 16" fill="none" stroke="#fff" stroke-width="1.1"><circle cx="8" cy="8" r="6.5"/><ellipse cx="8" cy="8" rx="2.8" ry="6.5"/><path d="M1.5 8h13M2.5 5h11M2.5 11h11"/></svg>www.wohnglanz-beispiel.at</li>
    </ul>
    <div class="double-rule" style="top:923px"></div>
    <div class="bank-details">
      <div><b>IBAN:</b> AT31 4817 2964 0058 2316</div>
      <div><b>BIC:</b> GLMTAT44XXX</div>
      <div><b>FN:</b> XXXXXXX</div>
      <div><b>UID:</b> XXXXXXX</div>
    </div>
    <div class="double-rule" style="top:1058px"></div>
  </aside>

  <main class="content">
    <div class="brand">
      <div class="brand-name">WOHNGLANZ</div>
      <div class="brand-tagline">eine Marke der KEV Wohnbau &amp; Grundstücksentwicklung GmbH</div>
    </div>
    <div class="date">10 December, 2021</div>
    <div class="recipient">STEFAN HOLLAUER</div>
    <div class="recipient-title">Cheif Executive Officer</div>
    <div class="body-text">
      <p>
        <span class="line">Contrary to popular belief, Lorem Ipsum is not simply random text. It has roots</span>
        <span class="line">in a piece of classical Latin literature from 45 BC, making it over 2000 years old.</span>
        <span class="line">Herbert Linsmayer, a Latin professor at Larchmont College in Oregon,</span>
        <span class="line last">looked up one of the more obscure Latin words, consectetur.</span>
      </p>
      <p>
        <span class="line">Lorem Ipsum comes from sections 1.10.32 and 1.10.33 of "de Finibus Bonorum</span>
        <span class="line">et Malorum" (The Extremes of Good and Evil) by Varronius, written in 45 BC. This</span>
        <span class="line">book is a treatise on the theory of ethics, very popular during the Renaissance.</span>
        <span class="line last">The first line of Lorem Ipsum.</span>
      </p>
      <p>
        <span class="line">The standard chunk of Lorem Ipsum used since the 1500s is reproduced below</span>
        <span class="line last">for those interested.</span>
      </p>
    </div>
    <div class="closing">Best Regards</div>
    <div class="signature" role="img" aria-label="Handwritten signature of the sender"></div>
  </main>

  <footer class="footer">
    <div class="company">KEV Wohnbau &amp; Grundstücksentwicklung GmbH</div>
    <div class="bank">Sparkasse Almtal, Bergländer Sparkasse from 1882, Genossenschaftskasse</div>
    <div class="bank">Anton-Weissauer-Strasse 7, 6391 Talbrunn</div>
  </footer>
</div>
</body>
</html>
```